PowerPoint template designs for my business

BrightPath is an educational services company that provides consulting and strategic planning services for Christian schools. We regularly produce webinars and other in-person presentations and would like our own PowerPoint templates to use for these presentations. We are looking for Master Slides and themes which incorporate our corporate image. See our logo and color palate in the uploaded files.

```html
<!DOCTYPE html>
<html lang="en">
<head>
<meta charset="utf-8">
<title>BrightPath Presentation Templates</title>
<link href="https://fonts.googleapis.com/css2?family=Poppins:ital,wght@0,300;0,400;0,500;0,600;0,700;1,400&display=swap" rel="stylesheet">
<style>
:root{
  --red:#e3202a;
  --deep-red:#a5141c;
  --maroon:#7a0f16;
  --ink:#1b1b1b;
  --text:#3a3a3a;
  --muted:#6b6b6b;
  --rule:#d9d9d9;
  --bar:#141414;
  --paper:#ffffff;
}
*{box-sizing:border-box;margin:0;padding:0}
html,body{width:1200px;height:807px;overflow:hidden;background:var(--paper)}
body{font-family:'Poppins',sans-serif;color:var(--text);position:relative}
.slide{position:absolute;width:349px;height:196px;background:var(--paper);overflow:hidden;box-shadow:0 4px 14px rgba(0,0,0,.22)}
.c1{left:33px}.c2{left:424px}.c3{left:814px}
.r1{top:52px}.r2{top:306px}.r3{top:560px}
.abs{position:absolute}
.brand{position:absolute;right:6px;top:6px;font-size:12px;font-weight:300;color:var(--maroon);letter-spacing:-.2px}
.title{position:absolute;font-weight:600;color:var(--ink);font-size:9.5px;line-height:1.5;white-space:nowrap}
.title .bar{color:var(--red);font-weight:400}
.footer{position:absolute;left:5px;right:0;bottom:4px;height:10px;display:flex;align-items:center;gap:4px}
.footer .globe{width:8px;height:8px;border-radius:50%;background:var(--deep-red);flex:none}
.footer .url{font-size:4.3px;color:var(--muted);flex:none;white-space:nowrap}
.footer .line{flex:1;height:.5px;background:var(--deep-red);margin:0 5px}
.footer .page{background:var(--deep-red);color:#fff;font-size:4px;padding:0 4px;height:10px;display:flex;align-items:center;white-space:nowrap;flex:none}
.photo{position:absolute}
.small{font-size:4.6px;line-height:1.6;color:var(--text)}
/* hero */
.hero-bg{inset:0;background:linear-gradient(100deg,#2a2a2a 0%,#4a4a4a 45%,#6d625c 70%,#3a3a3a 100%)}
.hero-url{position:absolute;right:21px;top:20px;color:#fff;font-size:6px;white-space:nowrap}
.hero-url span{color:var(--red)}
.hero-rule{position:absolute;right:0;top:31px;width:76px;height:.5px;background:var(--red)}
.hero-lead{position:absolute;left:11px;top:113px;color:#fff;font-size:10.5px;font-weight:300;white-space:nowrap}
.hero-key{position:absolute;left:11px;top:126px;color:var(--red);font-size:12px;font-weight:700;white-space:nowrap}
.hero-note{position:absolute;left:11px;top:157px;width:130px;color:#eee;font-size:4.3px;font-style:italic;line-height:1.7}
.hero-mark{position:absolute;right:11px;bottom:14px;color:#fff;font-size:24px;font-weight:300;letter-spacing:-.5px;white-space:nowrap}
/* agenda */
.agenda-item{position:absolute;left:158px;width:126px;height:17px;background:var(--bar);box-shadow:1px 1px 2px rgba(0,0,0,.35);color:#fff;font-size:4.3px;display:flex;align-items:center;padding-left:9px;white-space:nowrap}
.agenda-item .num{position:absolute;right:0;top:0;width:21px;height:17px;background:var(--deep-red);display:flex;align-items:center;justify-content:center;font-weight:600}
/* ideas */
.step{position:absolute;left:30px;width:135px}
.step .dash{width:12px;height:.7px;background:var(--ink);margin-bottom:3px}
.step h4{font-size:6.5px;font-weight:600;color:var(--ink);line-height:1.2}
.step p{font-size:3.9px;line-height:1.7;color:var(--text);margin-top:2px}
/* services */
.svc{position:absolute;top:75px;width:100px;text-align:center}
.svc .icon{width:22px;height:22px;margin:0 auto;border-radius:4px}
.svc h4{font-size:7px;font-weight:600;color:var(--ink);margin-top:12px}
.svc .dash{width:12px;height:.6px;background:var(--ink);margin:3px auto 5px}
.svc p{font-size:4px;line-height:1.7;color:var(--text)}
.svc-div{position:absolute;top:65px;width:.5px;height:108px;background:var(--rule)}
/* partners */
.grid{position:absolute;left:10px;top:40px;width:318px;height:129px;display:grid;grid-template-columns:82px 81px 74px 81px;grid-template-rows:37px 45px 47px}
.cell{display:flex;align-items:center;justify-content:center;border-color:var(--rule);border-style:solid;border-width:0}
.cell.rb{border-right-width:.5px}.cell.bb{border-bottom-width:.5px}
.badge{background:#8a8a8a}
</style>
</head>
<body>

<!-- Cover -->
<section class="slide c1 r1">
  <div class="photo hero-bg" role="img" aria-label="Smiling educator with curly hair in a dim library"></div>
  <div class="hero-url">www.<span>brightpath-edu</span>.com</div>
  <div class="hero-rule"></div>
  <div class="hero-lead">Empowering schools to</div>
  <div class="hero-key">achieve their next great fit</div>
  <p class="hero-note">One key trait unifies strong schools of all sizes: the drive to be better. BrightPath will help you get across your finish line and beyond.</p>
  <div class="hero-mark">BrightPath</div>
</section>

<!-- Agenda -->
<section class="slide c2 r1">
  <div class="brand">BrightPath</div>
  <div class="title" style="left:84px;top:89px;font-size:10px"><span class="bar">|</span> Agenda <span class="bar">|</span></div>
  <div class="agenda-item" style="top:34px">01.&nbsp; Agenda<span class="num">01</span></div>
  <div class="agenda-item" style="top:57px">02.&nbsp; Mission &amp; Vision<span class="num">02</span></div>
  <div class="agenda-item" style="top:80px">03.&nbsp; Our Statistics<span class="num">03</span></div>
  <div class="agenda-item" style="top:102px">04.&nbsp; Page Break<span class="num">04</span></div>
  <div class="agenda-item" style="top:125px">05.&nbsp; Perspiciatis Unde<span class="num">05</span></div>
  <div class="agenda-item" style="top:148px">06.&nbsp; What We Achieve<span class="num">06</span></div>
  <div class="footer"><span class="globe"></span><span class="url">www.brightpath-edu.com</span><span class="line"></span><span class="page">Page 02</span></div>
</section>

<!-- About -->
<section class="slide c3 r1">
  <div class="brand">BrightPath</div>
  <div class="title" style="left:25px;top:55px;font-size:9.5px"><span class="bar">|</span> About Us <span class="bar">|</span></div>
  <p class="small abs" style="left:26px;top:85px;width:100px;text-align:justify">Together, we're ensuring education bears the image of Christ – by growing exceptional leaders, effective school dynamics, and expanded access for more students.</p>
  <div class="photo" style="left:146px;top:30px;width:101px;height:135px;background:linear-gradient(160deg,#d8d6d2,#8d8880)" role="img" aria-label="Hands typing on a laptop"></div>
  <div class="photo" style="left:248px;top:30px;width:101px;height:67px;background:linear-gradient(160deg,#9a8f84,#4f5b68)" role="img" aria-label="Partners meeting around a table"></div>
  <div class="photo" style="left:248px;top:98px;width:101px;height:67px;background:linear-gradient(160deg,#5e5a55,#c9c2b5)" role="img" aria-label="Notebook and pen on a meeting table"></div>
  <div class="footer"><span class="globe"></span><span class="url">www.brightpath-edu.com</span><span class="line"></span><span class="page">Page 03</span></div>
</section>

<!-- Ideas -->
<section class="slide c1 r2">
  <div class="brand">BrightPath</div>
  <div class="title" style="left:8px;top:9px;font-size:9.5px"><span class="bar">|</span> Powerful ideas come from multiplied minds.<br>&nbsp; We assign two partners to every client. <span class="bar">|</span></div>
  <div class="step" style="top:50px"><div class="dash"></div><h4>Find the need</h4><p>We ask great questions to uncover the full picture of what's needed. Then pick the duo to spur ideas and cover the blindspots.</p></div>
  <div class="step" style="top:99px"><div class="dash"></div><h4>Hit the mark</h4><p>Solutions are found as a collaborative effort of the client team and BrightPath partner duo, with clear and actionable steps.</p></div>
  <div class="step" style="top:141px"><div class="dash"></div><h4>Look ahead</h4><p>Consulting doesn't stop at delivery. BrightPath helps clients see through the process and prepare for secondary efforts.</p></div>
  <div class="photo" style="left:217px;top:47px;width:47px;height:59px;background:linear-gradient(180deg,#b9a996,#7f8a98)" role="img" aria-label="Portrait of a partner in a light sweater"></div>
  <div class="photo" style="left:267px;top:47px;width:47px;height:59px;background:linear-gradient(180deg,#6e6158,#55565a)" role="img" aria-label="Portrait of a partner in a grey blazer"></div>
  <p class="abs" style="left:215px;top:117px;width:102px;font-size:5px;line-height:1.75;color:var(--ink)">The chemistry of our team is not idle talk, but real value tailored to a need. Every client is given a specific combination of leaders. 6 leaders. 15 combinations. That's higher power.</p>
  <div class="footer"><span class="globe"></span><span class="url">www.brightpath-edu.com</span><span class="line"></span><span class="page">Page 04</span></div>
</section>

<!-- Together -->
<section class="slide c2 r2">
  <div class="brand">BrightPath</div>
  <div class="title" style="left:20px;top:9px;font-size:9.5px"><span class="bar">|</span> What brought us together? <span class="bar">|</span></div>
  <p class="abs" style="left:21px;top:56px;width:125px;font-size:4.2px;line-height:1.85;color:var(--ink)">Though the moment of realization looked different for each partner, we arrived at a similar core belief in our educational careers—that more needs to be done. It is a realization shared over phone calls, conferences, and meetings between our partners across years of interactions and friendships.</p>
  <p class="abs" style="left:21px;top:113px;width:125px;font-size:4.2px;line-height:1.85;color:var(--ink)">The name of God needs to grow, and the school is where it starts. The world needs exceptional our schools because it needs well-educated, biblically anchored and morally clear young people grounded in the Truth. And from this reality, BrightPath was born.</p>
  <div class="photo" style="left:151px;top:39px;width:179px;height:115px;clip-path:polygon(38% 0,100% 0,100% 100%,0 100%);background:linear-gradient(135deg,#7a6a5c,#c8c0b4 55%,#6c7b70)" role="img" aria-label="Partners talking in an office"></div>
  <div class="footer"><span class="globe"></span><span class="url">www.brightpath-edu.com</span><span class="line"></span><span class="page">Page 05</span></div>
</section>

<!-- Break -->
<section class="slide c3 r2">
  <div class="photo" style="inset:0;background:linear-gradient(180deg,#b4454a 0%,#a2363c 45%,#8d2a30 70%,#7a2228 100%)" role="img" aria-label="Wooden pier on a calm lake at sunset, red tinted"></div>
  <div class="abs" style="left:19px;top:85px;color:#fff;font-size:9.5px;font-weight:600;line-height:1.5;white-space:nowrap"><span style="font-weight:300">|</span> Whatever you need,<br>&nbsp; we'll be right next to you. <span style="font-weight:300">|</span></div>
  <div class="abs" style="right:6px;bottom:5px;color:#fff;font-size:15px;font-weight:300">BrightPath</div>
</section>

<!-- Services -->
<section class="slide c1 r3">
  <div class="brand">BrightPath</div>
  <div class="title" style="left:19px;top:10px;font-size:9.5px"><span class="bar">|</span> Our Services <span class="bar">|</span> <span style="font-size:6.5px;font-weight:500">For leaders. For boards. For any school need.</span></div>
  <p class="abs" style="left:20px;top:31px;width:230px;font-size:4.2px;line-height:1.7;color:var(--ink)">BrightPath works with both sides of the equation, because we've been in both camps. You'll get solutions that consider the realities of your situation.</p>
  <div class="svc" style="left:12px"><div class="icon" style="background:#e8866f" role="img" aria-label="Talent search icon"></div><h4>Talent</h4><div class="dash"></div><p>Great leadership changes everything. Whether you're looking for a job or looking for your next leader, BrightPath can help you get there.</p></div>
  <div class="svc-div" style="left:118px"></div>
  <div class="svc" style="left:125px"><div class="icon" style="background:#f0b54a" role="img" aria-label="Consulting desk icon"></div><h4>Consulting</h4><div class="dash"></div><p>There are endless ways to make positive changes, but not always the bandwidth or know-how. Imagine what you could do with a trusted voice at your side?</p></div>
  <div class="svc-div" style="left:232px"></div>
  <div class="svc" style="left:238px"><div class="icon" style="background:#4a6fa5" role="img" aria-label="Management team icon"></div><h4>Management</h4><div class="dash"></div><p>BrightPath is actively developing standards for the greater staff of school administrators. You can save on wasted time and effort.</p></div>
  <div class="footer"><span class="globe"></span><span class="url">www.brightpath-edu.com</span><span class="line"></span><span class="page">Page 07</span></div>
</section>

<!-- Partners -->
<section class="slide c2 r3">
  <div class="brand">BrightPath</div>
  <div class="title" style="left:20px;top:10px;font-size:9.5px"><span class="bar">|</span> Our Partners <span class="bar">|</span></div>
  <div class="grid">
    <div class="cell rb bb"><span class="badge" style="width:14px;height:18px;border-radius:3px"></span></div>
    <div class="cell rb bb"><span class="badge" style="width:46px;height:12px;background:#9a9a9a"></span></div>
    <div class="cell rb bb"><span class="badge" style="width:20px;height:20px;border-radius:50%"></span></div>
    <div class="cell bb"><span class="badge" style="width:16px;height:16px;border-radius:50%;background:#a0a0a0"></span></div>
    <div class="cell rb bb"><span class="badge" style="width:50px;height:7px;background:#555"></span></div>
    <div class="cell rb bb"><span class="badge" style="width:22px;height:22px;border-radius:50%;background:#333"></span></div>
    <div class="cell rb bb"><span class="badge" style="width:38px;height:20px;background:#777"></span></div>
    <div class="cell bb"><span class="badge" style="width:52px;height:9px;background:#8a8a8a"></span></div>
    <div class="cell rb"><span class="badge" style="width:44px;height:18px;background:#3a3a3a"></span></div>
    <div class="cell rb"><span class="badge" style="width:24px;height:22px;background:#777"></span></div>
    <div class="cell rb"><span class="badge" style="width:46px;height:20px;background:#2a2a2a"></span></div>
    <div class="cell"></div>
  </div>
  <div class="footer"><span class="globe"></span><span class="url">www.brightpath-edu.com</span><span class="line"></span><span class="page">Page 08</span></div>
</section>

<!-- Contact -->
<section class="slide c3 r3">
  <div class="photo" style="inset:0;background:linear-gradient(120deg,#8a1118 0%,#6d0c12 50%,#4d070c 100%)" role="img" aria-label="Group of colleagues laughing around a table, red tinted"></div>
  <div class="hero-url">www.<span>brightpath-edu</span>.com</div>
  <div class="hero-rule"></div>
  <div class="hero-lead" style="top:65px">Contact BrightPath</div>
  <div class="hero-key" style="top:81px;font-size:13px">Let's make a plan.</div>
  <p class="hero-note" style="top:109px;width:150px">We're called BrightPath for a number of reasons, but the first one is you. Whatever your next thing is, it starts right here.</p>
  <div class="hero-mark" style="font-size:28px;bottom:10px">BrightPath</div>
</section>

</body>
</html>
```